Billboard to promote Harwell County, NC

I would like a billboard designed for the Chamber of Commerce. The size of the board is 10'h by 24'w. I would like our logo colors used and IF space permits, include our logo. I want to board to be very easy to read with a simplistic message of #StayWithHarwell, Invest in this community, Shop, Dine, Live. I would like our web address to scroll the bottom of the board, www.TheHarwellChamber.example

Target Market(s)

Local residents and visitors

Industry/Entity Type

Chamber Of Commerce

Requirements
Must have
• Quick message
• Easy to read
• Bold type
Nice to have
• Our logo, if space permits.
Should not have
• Should not be too busy or hard to read. People are driving by at 55-65 miles per hour.

```html
<!DOCTYPE html>
<html lang="en">
<head>
<meta charset="utf-8">
<title>Harwell Chamber Billboard</title>
<link rel="stylesheet" href="https://fonts.googleapis.com/css2?family=Bebas+Neue&family=Lato:wght@700&display=swap">
<style>
  :root {
    --page-bg: #1b1b1b;
    --board-blue: #0a4ea0;
    --board-blue-light: #1266bd;
    --panel-white: #ffffff;
    --accent-orange: #f7a418;
    --ink-navy: #1e2c83;
    --text-white: #ffffff;
  }
  * { margin: 0; padding: 0; box-sizing: border-box; }
  html, body {
    width: 1200px;
    height: 1000px;
    overflow: hidden;
    background: var(--page-bg);
  }
  .canvas {
    position: relative;
    width: 1200px;
    height: 1000px;
  }
  .billboard {
    position: absolute;
    left: 50px;
    top: 271px;
    width: 1100px;
    height: 459px;
    overflow: hidden;
  }
  .billboard-shapes {
    position: absolute;
    inset: 0;
    width: 100%;
    height: 100%;
  }
  .brand {
    position: absolute;
    left: 40px;
    top: 92px;
    width: 346px;
    text-align: center;
    font-family: "Lato", Arial, sans-serif;
    font-weight: 700;
    color: var(--ink-navy);
  }
  .brand-mark {
    display: block;
    width: 94px;
    height: 94px;
    margin: 0 auto 14px;
    border-radius: 50%;
    background: var(--board-blue);
  }
  .brand-name {
    display: block;
    font-size: 36px;
    line-height: 1;
    letter-spacing: 0.5px;
  }
  .brand-sub {
    display: block;
    font-size: 17px;
    line-height: 1;
    letter-spacing: 3.4px;
    margin-top: 6px;
  }
  .message {
    position: absolute;
    left: 500px;
    width: 540px;
    text-align: center;
    font-family: "Bebas Neue", Impact, sans-serif;
    line-height: 1;
    white-space: nowrap;
  }
  .hashtag { top: 88px; font-size: 68px; color: var(--text-white); }
  .invite  { top: 155px; font-size: 68px; color: var(--text-white); }
  .tagline { top: 233px; font-size: 94px; color: var(--accent-orange); letter-spacing: 1px; }
  .web-address {
    top: 396px;
    font-size: 48px;
    color: var(--ink-navy);
    letter-spacing: 0.5px;
  }
</style>
</head>
<body>
<main class="canvas">
  <section class="billboard" aria-label="Harwell Chamber billboard">
    <svg class="billboard-shapes" viewBox="0 0 820 342" preserveAspectRatio="none" aria-hidden="true">
      <rect class="field" x="0" y="0" width="820" height="342" fill="var(--board-blue)"/>
      <polygon class="field-sweep" points="170,287 820,70 820,287" fill="var(--board-blue-light)" opacity="0.55"/>
      <polygon class="brand-panel" points="0,0 272,0 350,287 0,287" fill="var(--panel-white)"/>
      <polygon class="address-band" points="185,342 240,287 820,287 820,342" fill="var(--accent-orange)"/>
    </svg>

    <div class="brand">
      <span class="brand-mark"></span>
      <span class="brand-name">HARWELL CHAMBER</span>
      <span class="brand-sub">OF COMMERCE &amp; TOURISM</span>
    </div>

    <p class="message hashtag">#STAYWITHHARWELL,</p>
    <p class="message invite">INVEST IN THIS COMMUNITY</p>
    <p class="message tagline">SHOP.DINE.LIVE.</p>
    <p class="message web-address">WWW.THEHARWELLCHAMBER.EXAMPLE</p>
  </section>
</main>
</body>
</html>
```